Chartered accountants trying to make boring information more appealing!

We are UK based chartered accountants with various specialist areas of expertise. We need a template for a monthly mailer that we send to our clients and contacts to keep them updated with key financial news. The update is called Amber Reef and we'd like it to fit on one page of A4 that we can then drop text into. We would like it to be more appealing than just the usual calculators and audit papers associated with accountants. Our brand colours are blue and green.

Target Market(s)

Our clients range from small businesses to large pension fund trustees, charities and individuals. It must appeal to everyone.

Industry/Entity Type

Accounting

Colors
34a7d8
33b8a4
3277b5

Requirements
Must have
• Space for text. The title 'Amber Reef'. Our logo.
Nice to have
• Sky's the limit!
Should not have
• Shouldn't look homemade. I've attached an old one done in house - please avoid this!

```html
<!DOCTYPE html>
<html lang="en">
<head>
<meta charset="utf-8">
<title>Amber Reef Update – March 2016</title>
<link rel="stylesheet" href="https://fonts.googleapis.com/css2?family=Open+Sans:ital,wght@0,300;0,400;0,600;0,700;1,300;1,400&display=swap">
<style>
:root{
  --sky:#34a7d8;
  --teal:#33b8a4;
  --navy:#3277b5;
  --ink:#3c3c3c;
  --tint:#e7f3fa;
  --tint-deep:#cfe6f4;
  --line:#9fcbe6;
  --white:#ffffff;
}
*{box-sizing:border-box;margin:0;padding:0}
html,body{width:849px;height:1200px;overflow:hidden;background:var(--white)}
body{font-family:"Open Sans",Arial,sans-serif;color:var(--ink);position:relative}
.page{position:relative;width:849px;height:1200px;overflow:hidden}
.top-wave{position:absolute;top:0;left:0;width:849px;height:120px}
.web{position:absolute;top:10px;right:34px;font-size:12px;font-weight:700;color:var(--navy)}
.title{position:absolute;top:34px;left:40px;font-size:27px;color:var(--sky);letter-spacing:.2px;white-space:nowrap}
.title .month{font-weight:300}
.title .name{font-weight:700;color:var(--navy)}
.title .cont{font-weight:300;font-style:italic;font-size:22px;color:var(--sky)}
.psa{position:absolute;top:80px;left:36px;width:777px;height:432px;background:var(--tint);border-radius:4px;padding:12px 14px}
.psa h2{font-size:13.5px;font-weight:700;color:var(--navy);margin-bottom:4px}
p{font-size:11.6px;line-height:1.55;margin-bottom:9px}
.psa-table{width:560px;border-collapse:collapse;margin:4px 0 10px;font-size:11px;line-height:1.45;background:var(--white)}
.psa-table th{background:var(--tint-deep);text-align:left;font-weight:700;color:var(--navy);padding:4px 8px;border:1px solid var(--line)}
.psa-table td{padding:4px 8px;border:1px solid var(--line);vertical-align:top}
.psa-table td:first-child{width:170px}
.band{position:absolute;top:524px;left:36px;width:777px;height:34px;border-radius:4px;background:linear-gradient(90deg,var(--teal),var(--sky));padding:0 14px;display:flex;align-items:center}
.band h2{font-size:19px;font-weight:700;color:var(--white)}
.pension{position:absolute;top:566px;left:50px;width:750px}
.footer{position:absolute;left:0;bottom:0;width:849px;height:94px;background:var(--navy);color:var(--white);display:flex;padding:14px 36px 0 40px}
.footer-left{width:420px;font-size:12px;line-height:1.5}
.footer-left strong{font-weight:700}
.footer-right{margin-left:auto;width:310px}
.firm{font-size:14px;font-weight:700;margin-bottom:3px;display:flex;align-items:center;gap:7px}
.firm .dot{width:11px;height:11px;background:var(--teal);border-radius:50%}
.firm-address{font-size:10.8px;line-height:1.45}
.contacts{display:flex;gap:14px;font-size:10.8px;margin-top:3px;align-items:center}
.contacts span{display:flex;align-items:center;gap:4px}
</style>
</head>
<body>
<div class="page">
  <svg class="top-wave" viewBox="0 0 849 120" aria-hidden="true">
    <path d="M0 0H849V60C700 95 560 40 420 70S150 110 0 80Z" fill="#eef7fc"/>
  </svg>
  <div class="web">www.hartwellpartners.biz</div>
  <h1 class="title"><span class="month">MARCH 2016</span> <span class="name">AMBER REEF UPDATE</span> <span class="cont">continued.....</span></h1>

  <section class="psa">
    <h2>PSA deadlines and payments</h2>
    <p>If HM Revenue and Customs approve your PSA before the start of the tax year, you can include any expenses and benefits contained in the agreement. If it is approved after the start of the tax year, you might still need to report some items (such as gift vouchers) separately using the normal year end forms P9D and P11D.</p>
    <p>The table below shows what you need to report separately for the tax year 2015 to 2016:</p>
    <table class="psa-table">
      <tr><th>PSA approval date</th><th>Items to be reported separately</th></tr>
      <tr><td>Up to 5 April 2016</td><td>Items provided before the agreement date that you've already included in your employee's tax code, or deducted (or should have deducted) PAYE tax on</td></tr>
      <tr><td>Between 6 April 2016 &amp; 6 July 2016</td><td>Items provided during the tax year that you've already included in your employee's tax code, or deducted (or should have deducted) PAYE tax on</td></tr>
      <tr><td>After 6 July 2016</td><td>You can't apply for a PSA for tax year 2015 to 2016</td></tr>
    </table>
    <p>You must pay any tax and National Insurance owed under a PSA by 22 October after the tax year the PSA applies to (or 19 October if you pay by post).</p>
    <p>Any application for a PSA must be made in writing to HMRC within the above deadlines and must contain details of the expenses and benefits you wish to be included. Once approved, you'll need to calculate the amount of tax and National Insurance payable under the PSA and submit this back to HMRC who will confirm your calculations and payment details between 6 July and 19 October.</p>
    <p>PSA's must be renewed every year before 6 July and, whilst this sounds like a complicated process, it can provide significant time and cost savings to you. If you would like more information or assistance in applying for a PSA, please contact a member of our team.</p>
  </section>

  <div class="band"><h2>Pension Contributions</h2></div>

  <section class="pension">
    <p>Gordon Ashcroft has dropped plans to end or alter tax relief on pension contributions.</p>
    <p>A proposed scheme would have scrapped upfront relief, worth an estimated £21bn to savers, but made pension pot withdrawals tax free. An alternative option was to set a flat rate of tax relief, which may have been unpopular with higher earners.</p>
    <p>Campaigners suggest that the Chancellor has missed a "huge opportunity" to tackle obvious pension inequality and help the lower paid, but others say he was right to protect existing reliefs and that radical reforms would have created new risks and imposed new administrative burdens on employers. Mr Ashcroft had been expected to unveil changes in the Budget on 16 March, but a Treasury source said it was "not the right time".</p>
    <p>Under the current system, pension savers receive tax relief at the same rate as their income tax – meaning basic rate taxpayers receive relief at 20% and higher rate taxpayers at 40% or 45%. The proposal to introduce arrangements similar to an ISA with no tax relief on contributions but with withdrawals free of tax, would have given a significant short-term boost to the government at the expense of lower tax revenue later. An alternative option considered by the Treasury was for flat rate relief, which would have benefited basic rate taxpayers and cut reliefs for higher earners.</p>
    <p>The prospect of radical reform has also been opposed by the pensions industry with a period of considerable change having taken place in recent years. Automatic enrolment for employees into workplace pensions has accelerated since its introduction in 2012 and, since 2015, people aged 55 and over have been allowed to take their retirement pots in the form they want, rather than being required to buy an annuity retirement income.</p>
    <p>We will provide further information on the Budget, once it has been announced on 16 March.</p>
  </section>

  <footer class="footer">
    <div class="footer-left">For more information on the subjects covered in this paper, or to arrange a consultation, please contact <strong>Daniel Pryce</strong> at <strong>daniel@hartwellpartners.biz</strong> or call us on <strong>0116 555 0140</strong></div>
    <div class="footer-right">
      <div class="firm"><span class="dot"></span>The Hartwell Partnership Limited</div>
      <div class="firm-address">Ashby House, Kestrel Way,<br>Riverside Business Park, Leicester, LE2 9XQ</div>
      <div class="contacts">
        <span><svg width="10" height="10" viewBox="0 0 24 24" aria-hidden="true"><path fill="#fff" d="M6.6 10.8a15 15 0 0 0 6.6 6.6l2.2-2.2a1 1 0 0 1 1-.25 11.4 11.4 0 0 0 3.6.6 1 1 0 0 1 1 1V20a1 1 0 0 1-1 1A17 17 0 0 1 3 4a1 1 0 0 1 1-1h3.5a1 1 0 0 1 1 1c0 1.25.2 2.45.6 3.6a1 1 0 0 1-.25 1z"/></svg>0116 555 0140</span>
        <span><svg width="11" height="9" viewBox="0 0 24 18" aria-hidden="true"><rect x="1" y="1" width="22" height="16" rx="2" fill="none" stroke="#fff" stroke-width="2"/><path d="M1 2l11 8 11-8" fill="none" stroke="#fff" stroke-width="2"/></svg>post@hartwellpartners.biz</span>
      </div>
    </div>
  </footer>
</div>
</body>
</html>
```